Packaging design - PROTEIN BALLS

PACKAGING
The packaging is a round carton roll, size: Ø73x180 mm, mockup sample enclosed, The label on the carton roll should have a size of 225x178 mm (width x height)

PRODUCT
Chrunchy, cheesy PROTEIN BALLS (100% pure cheese) with a huge amount of protein (65%), a lot of calcium and very low carbogydrates (3%). Diameter about 1.5 cm.

DESIGN
Since our customers are very sporty people, runner, bodybuilder, etc. The design must fit to this sporty customer segment.

FILES
We need the open data for InDesign with all fonts and pictures. If there are licenses tu buy, we will do it.

SUMMARY
1. SNACK
• Crunchy cheese balls with a diameter of about 1.5cm
• 3 different flavors: "Swiss Alpine Salt", "Provencale" and "Hot Chili"
• High in Protein (65%) and Calcium (2%)
• Low in carbohydrates (3%)

2. PACKAGING
• Carton roll, size: Ø73x180 mm
• Background can be every color, but we think a black one will be high premium.
• Maybe different sports are represented in the background, maybe also cheese
• Be creative
• Label applied, size: 225x178 mm

3. DESIGN
• Product name = (Cheese) PROTEIN BALLS
• 3 different colors for the 3 flavors "Swiss Alpine Salt", "Provencale" and "Hot Chili"
• HighProtein, High Calcium and LowCarb must be pointed out on the front
• Swissness: Swiss made must be pointed out
• fresh and young design, most customers are sporty people, pumper with a strong body awareness

Target Market(s)

TARGET CUSTOMER
Our main customers are extremely sporty people, who work very hard on their muscles and fitness, most of them are runners, cross fitnesser, bodybuilders, etc We will launch the product in fitness centers, in supplement shops and we are planning to make some stories with sporty influencer.

Font styles to use
Serif
Sans Serif

Requirements
Must have
• Cheese, naturalness, healthy, PROTEIN balls, muscles, Swissness must showed on the product.

```html
<!DOCTYPE html>
<html lang="en">
<head>
<meta charset="utf-8">
<title>Cheese Protein Balls – Hot Chili label</title>
<link rel="stylesheet" href="https://fonts.googleapis.com/css2?family=Oswald:wght@500;600&family=Yellowtail&family=Amatic+SC:wght@700&display=swap">
<style>
  :root {
    --page: #ffffff;
    --label-dark: #2a2a2c;
    --label-mid: #3a3a3d;
    --ink-light: #f2f0ec;
    --cheese-gold: #c9b48e;
    --chili-red: #b3312d;
    --chili-red-dark: #8e2220;
    --badge-light: #e6e4e1;
    --sketch: #6a6a6e;
  }
  * { margin: 0; padding: 0; box-sizing: border-box; }
  html, body { width: 1200px; height: 1200px; overflow: hidden; background: var(--page); }
  .canvas { position: relative; width: 1200px; height: 1200px; }

  .label {
    position: absolute; left: 100px; top: 205px; width: 1000px; height: 790px;
    background: linear-gradient(90deg, var(--label-dark) 0%, var(--label-mid) 50%, var(--label-dark) 100%);
    overflow: hidden;
  }

  .front { position: absolute; left: 290px; top: 0; width: 420px; height: 790px; text-align: center; }

  .swiss-made {
    position: absolute; top: 30px; left: 0; right: 0;
    display: flex; justify-content: center; align-items: center; gap: 10px;
    font-family: "Oswald", sans-serif; font-weight: 500; font-size: 22px;
    letter-spacing: 2px; color: var(--ink-light);
  }
  .swiss-made svg { width: 38px; height: 32px; }

  .mountain-art {
    position: absolute; top: 78px; left: 0; width: 420px; height: 260px;
    background: radial-gradient(ellipse at 50% 40%, rgba(130,130,135,0.35) 0%, rgba(90,90,95,0.15) 55%, rgba(0,0,0,0) 75%);
  }

  .flavour-family {
    position: absolute; top: 240px; left: 0; right: 0;
    font-family: "Yellowtail", cursive; font-size: 60px; color: var(--cheese-gold);
  }
  .product-name {
    position: absolute; top: 306px; left: 0; right: 0;
    font-family: "Oswald", sans-serif; font-weight: 600; font-size: 94px; line-height: 88px;
    letter-spacing: 2px; color: var(--ink-light); text-transform: uppercase;
  }
  .audience {
    position: absolute; top: 506px; left: 0; right: 0;
    font-family: "Oswald", sans-serif; font-weight: 500; font-size: 24px;
    letter-spacing: 3px; color: var(--ink-light);
  }

  .flavour-ribbon {
    position: absolute; top: 566px; left: 98px; width: 226px; height: 60px;
    background: var(--chili-red);
    font-family: "Yellowtail", cursive; font-size: 46px; line-height: 60px; color: var(--ink-light);
  }
  .chili-art {
    position: absolute; top: 570px; left: 300px; width: 70px; height: 100px;
    background: radial-gradient(ellipse at 50% 60%, var(--chili-red-dark) 0%, rgba(142,34,32,0.6) 45%, rgba(0,0,0,0) 72%);
  }

  .claims { position: absolute; top: 680px; left: 0; right: 0; display: flex; justify-content: center; gap: 14px; }
  .claim {
    width: 64px; height: 64px; border-radius: 50%;
    display: flex; align-items: center; justify-content: center;
    font-family: "Amatic SC", sans-serif; font-weight: 700; font-size: 17px; line-height: 15px;
    border: 2px solid var(--ink-light); box-shadow: 0 0 0 2px var(--label-dark), 0 0 0 3px rgba(255,255,255,0.4);
  }
  .claim--red { background: var(--chili-red); color: var(--ink-light); }
  .claim--light { background: var(--badge-light); color: var(--chili-red); }
</style>
</head>
<body>
<main class="canvas">
  <section class="label">
    <div class="front">
      <div class="swiss-made">
        <span>SWISS MADE</span>
        <svg viewBox="0 0 38 32" aria-hidden="true">
          <rect x="0" y="0" width="38" height="32" fill="var(--chili-red)"/>
          <rect x="16" y="7" width="6" height="18" fill="#fff"/>
          <rect x="10" y="13" width="18" height="6" fill="#fff"/>
        </svg>
      </div>
      <div class="mountain-art" role="img" aria-label="Sketched alpine mountain peak drawing"></div>
      <div class="flavour-family">Cheese</div>
      <h1 class="product-name">Protein<br>Balls</h1>
      <div class="audience">- FOR ATHLETES -</div>
      <div class="chili-art" role="img" aria-label="Illustration of red chili peppers"></div>
      <div class="flavour-ribbon">Hot Chili</div>
      <div class="claims">
        <div class="claim claim--red">LOW<br>CARB</div>
        <div class="claim claim--light">HIGH<br>PROTEIN<br>65%</div>
        <div class="claim claim--light">HIGH<br>CALCIUM</div>
      </div>
    </div>
  </section>
</main>
</body>
</html>
```